Velvor IT Services Business Card

Velvor IT Services are a Perth based IT Services company. We would like to incorporate our company logo (attached) and stick with the blue that is in that design. I would like a clean look design that isn't too busy, yet creates a lasting image that is instantly recognisable in the recipients mind.

Target Market(s)

The target audience is small/medium business owners.

Industry/Entity Type

Business

Font styles to use
Serif
Sans Serif

Colors

Designer to choose colors to be used in the design.

Requirements
Must have
• The design should include:
Business name: Velvor IT Services
Directors Name: Marcus Dredge
Phone Number: 0483 906 452
Email: support@velvorit.com.au
Website: www.velvorit.com.au

```html
<!DOCTYPE html>
<html lang="en">
<head>
<meta charset="utf-8">
<title>Velvor IT Services – Business Card</title>
<link rel="stylesheet" href="https://fonts.googleapis.com/css2?family=Lato:wght@300;400;700;900&display=swap">
<style>
  :root {
    --bg: #e9ebef;
    --card: #ffffff;
    --blue: #2f6fc0;
    --blue-deep: #1d4f9e;
    --blue-light: #3f8ad6;
    --text-blue: #4a78b8;
    --rule: #b9c3dc;
  }
  * { margin: 0; padding: 0; box-sizing: border-box; }
  html, body { width: 1200px; height: 913px; overflow: hidden; }
  body {
    background: var(--bg);
    font-family: "Lato", sans-serif;
    position: relative;
  }
  .card {
    position: absolute;
    width: 620px;
    height: 379px;
    background: var(--card);
    box-shadow: 0 8px 24px rgba(0,0,0,.18);
    overflow: hidden;
  }
  .card--front { left: 60px; top: 60px; }
  .card--back { left: 520px; top: 474px; }

  .brand {
    position: absolute;
    display: flex;
    align-items: center;
    gap: 10px;
    color: var(--blue);
    font-weight: 900;
    font-size: 24px;
    letter-spacing: .5px;
    white-space: nowrap;
  }
  .brand__mark {
    width: 16px; height: 16px;
    background: var(--blue);
  }
  .card--front .brand { left: 170px; top: 140px; }
  .card--back .brand { right: 40px; top: 40px; font-size: 22px; }

  .band {
    position: absolute;
    left: 0; right: 0;
    background: linear-gradient(90deg, var(--blue-deep), var(--blue) 60%, var(--blue-light));
  }
  .card--front .band { top: 268px; height: 40px; }
  .card--back .band { top: 290px; height: 38px; }

  .band__web {
    position: absolute;
    right: 26px; top: 50%;
    transform: translateY(-50%);
    color: #fff;
    font-size: 19px;
    font-weight: 400;
  }

  .divider {
    position: absolute;
    left: 150px; top: 92px;
    width: 440px; height: 2px;
    background: linear-gradient(90deg, rgba(185,195,220,0), var(--rule));
  }

  .contacts {
    position: absolute;
    right: 40px; top: 112px;
    list-style: none;
    text-align: right;
    color: var(--text-blue);
    font-size: 15px;
    font-weight: 300;
    line-height: 22px;
  }
  .contacts li { display: flex; justify-content: flex-end; align-items: center; gap: 8px; }
  .contacts svg { width: 13px; height: 13px; fill: var(--blue-deep); }

  .person {
    position: absolute;
    left: 40px; top: 178px;
  }
  .person__name {
    color: var(--blue-deep);
    font-weight: 900;
    font-size: 22px;
  }
  .person__role {
    color: var(--text-blue);
    font-weight: 300;
    font-size: 16px;
  }
  .address {
    position: absolute;
    left: 40px; top: 244px;
    display: flex; align-items: center; gap: 8px;
    color: var(--text-blue);
    font-size: 15px;
  }
  .address svg { width: 12px; height: 16px; fill: #1e2d4a; }
</style>
</head>
<body>

<section class="card card--front" aria-label="Card front">
  <div class="brand"><span class="brand__mark"></span>Velvor IT Services</div>
  <div class="band"><span class="band__web">www.velvorit.com.au</span></div>
</section>

<section class="card card--back" aria-label="Card back">
  <div class="brand"><span class="brand__mark"></span>Velvor IT Services</div>
  <div class="divider"></div>
  <ul class="contacts">
    <li>0483 906 452
      <svg viewBox="0 0 24 24"><path d="M6.6 10.8a15.1 15.1 0 0 0 6.6 6.6l2.2-2.2c.3-.3.7-.4 1-.2 1.1.4 2.3.6 3.6.6.6 0 1 .4 1 1V20c0 .6-.4 1-1 1A17 17 0 0 1 3 4c0-.6.4-1 1-1h3.5c.6 0 1 .4 1 1 0 1.3.2 2.5.6 3.6.1.3 0 .7-.2 1z"/></svg>
    </li>
    <li>support@velvorit.com.au
      <svg viewBox="0 0 24 24"><path d="M2 5h20v14H2z" fill="none" stroke="#1d4f9e" stroke-width="2"/><path d="M2 5l10 8 10-8" fill="none" stroke="#1d4f9e" stroke-width="2"/></svg>
    </li>
    <li>www.velvorit.com.au
      <svg viewBox="0 0 24 24"><circle cx="12" cy="12" r="9" fill="none" stroke="#1d4f9e" stroke-width="2"/><path d="M3 12h18M12 3c3 3 3 15 0 18M12 3c-3 3-3 15 0 18" fill="none" stroke="#1d4f9e" stroke-width="1.6"/></svg>
    </li>
  </ul>
  <div class="person">
    <p class="person__name">Marcus Dredge</p>
    <p class="person__role">Director</p>
  </div>
  <p class="address">
    <svg viewBox="0 0 12 16"><path d="M6 0a6 6 0 0 0-6 6c0 4.5 6 10 6 10s6-5.5 6-10a6 6 0 0 0-6-6zm0 8.5A2.5 2.5 0 1 1 6 3.5a2.5 2.5 0 0 1 0 5z"/></svg>
    14 Kestrel Rise Bedfordale WA 6112 au
  </p>
  <div class="band"></div>
</section>

</body>
</html>
```